Flyer Design

I need a flyer design for a new company based in Scotland called Snapwell Mite solution,s we want to provide a service power washing wheelie bins for the hotel and catering trade and domestic wheelie bins.We want a flyer with a few animated germs and Snapwell on the front we want to make out that by touching this flyer or the bin you may have come in contact with harmful germs including salmonella ecoli influenza and that you could potentially contaminate anything else you may touch including other people or risk cross contamination by spreading the germs to door handles etc.We also want a section of the flyer where clients can register their bins for cleaning.We need a basic registration form where our clients can write their postcode establishment name or house number.what day their bins are emptied.Our crew will follow the waste disposal vehicle and clean the bin when empty.The flyer should inform the client that a 4 wheele bin (dumpster) costs £10 for the first clean and £5 per subsequent clean and a 2 wheele bin (wheelie) costs £6 for the first clean and £3 per subsequent clean.The flyer should inform the client that they may register by texting their information to 07912448731.eg KT37QB the pub Black dumpster Tuesday.
Updates

The address and post code in original brief haven't to go on flyer and only Snapwell and the germ representation to be on the front of the flyer on the bottom 2 thirds as the top o As the top part will be under thr bin lid thanks Ewan.

Industry/Entity Type

Catering

Requirements
Must have
• The flyer must have only Snapwell and the germ logo on the front of the flyer.
The postcode and address from the brief hasn't to go on the flyer.
Nice to have
• A logo that's serious but jot frightening.

```html
<!DOCTYPE html>
<html lang="en">
<head>
<meta charset="utf-8">
<title>Snapwell Mite Solution – Flyer</title>
<link rel="stylesheet" href="https://fonts.googleapis.com/css2?family=Squada+One&family=Lato:wght@400;700&family=Roboto+Condensed:wght@700&display=swap">
<style>
  :root {
    --charcoal: #3d3d3f;
    --red: #e01f2b;
    --deep-red: #b3121d;
    --orange: #f26522;
    --white: #ffffff;
    --panel: #ececec;
    --photo-warm: #d6a437;
    --photo-cool: #7c7f84;
    --germ-purple: #b79ad6;
    --germ-green: #a9c53a;
    --germ-orange: #d1642a;
  }
  html, body { margin: 0; padding: 0; overflow: hidden; background: #f2f2f2; }
  .flyer {
    position: relative; width: 919px; height: 1200px; overflow: hidden;
    background: var(--charcoal); color: var(--white);
    font-family: "Lato", sans-serif;
  }
  .flyer-shapes { position: absolute; inset: 0; }
  .display { font-family: "Squada One", sans-serif; text-transform: uppercase; }
  .intro {
    position: absolute; left: 25px; top: 100px; margin: 0;
    font-size: 35px; line-height: 43px; font-weight: 400;
  }
  .brand-badge {
    position: absolute; left: 388px; top: 297px; width: 184px; height: 184px;
    display: flex; align-items: center; justify-content: center;
    font-family: "Roboto Condensed", sans-serif; font-weight: 700;
    font-size: 31px; color: var(--charcoal); text-transform: uppercase;
  }
  .headline {
    position: absolute; right: 26px; top: 300px; margin: 0; text-align: right;
    font-size: 74px; line-height: 69px; font-weight: 400;
  }
  .text-line {
    position: absolute; right: 32px; top: 545px; margin: 0;
    font-size: 21px; letter-spacing: 0.2px;
  }
  .text-line .phone { color: var(--deep-red); }
  .hazard {
    position: absolute; left: 28px; top: 612px; width: 820px; margin: 0;
    font-size: 20px; line-height: 29px;
  }
  .form-title {
    position: absolute; left: 22px; top: 756px; margin: 0;
    font-family: "Roboto Condensed", sans-serif; font-weight: 700; font-size: 34px;
  }
  .field {
    position: absolute; left: 42px; margin: 0;
    font-size: 23px; line-height: 26px; color: var(--white);
  }
  .form-note {
    position: absolute; left: 26px; top: 1050px; margin: 0; width: 290px;
    font-size: 13px; line-height: 19px; color: #333; text-align: center;
  }
  .prices { position: absolute; left: 0; top: 0; margin: 0; font-size: 21px; }
  .prices span.line { position: absolute; white-space: nowrap; }
  .price { color: var(--red); font-size: 32px; }
  .filler {
    position: absolute; left: 397px; top: 912px; margin: 0;
    font-size: 21px; line-height: 33px;
  }
  .web {
    position: absolute; right: 40px; top: 1145px; margin: 0;
    display: flex; align-items: center; gap: 8px;
    font-weight: 700; font-size: 27px;
  }
</style>
</head>
<body>
<main class="flyer">
  <svg class="flyer-shapes" width="919" height="1200" viewBox="0 0 919 1200">
    <defs>
      <linearGradient id="photo-tone" x1="0" y1="0" x2="1" y2="1">
        <stop offset="0" stop-color="var(--photo-cool)"/>
        <stop offset="0.5" stop-color="var(--photo-warm)"/>
        <stop offset="1" stop-color="#5c5f66"/>
      </linearGradient>
    </defs>
    <polygon role="img" aria-label="Photo of a refuse collection lorry with a worker emptying a bin"
      points="257,0 919,0 919,219 406,381" fill="url(#photo-tone)"/>
    <polygon class="intro-panel" points="0,0 257,0 406,381 0,594" fill="var(--red)"/>
    <polyline points="257,0 406,381 0,594" fill="none" stroke="var(--white)" stroke-width="9"/>
    <line x1="406" y1="381" x2="919" y2="219" stroke="var(--white)" stroke-width="9"/>
    <g role="img" aria-label="Cartoon purple germ character">
      <circle cx="822" cy="118" r="78" fill="var(--white)"/>
      <circle cx="822" cy="118" r="70" fill="var(--germ-purple)"/>
    </g>
    <circle cx="480" cy="389" r="96" fill="var(--white)"/>
    <circle cx="480" cy="389" r="80" fill="var(--orange)"/>
    <polygon class="text-band" points="140,530 890,530 890,590 108,590" fill="var(--red)"/>
    <polygon class="form-panel" points="0,725 300,725 345,905 319,1108 0,1108" fill="var(--panel)"/>
    <polygon class="form-header" points="0,756 330,756 361,806 0,806" fill="var(--charcoal)"/>
    <rect x="25" y="825" width="336" height="46" fill="var(--red)" stroke="var(--white)" stroke-width="2"/>
    <rect x="25" y="895" width="319" height="46" fill="var(--red)" stroke="var(--white)" stroke-width="2"/>
    <rect x="25" y="968" width="270" height="70" fill="var(--red)" stroke="var(--white)" stroke-width="2"/>
    <polygon class="footer-band" points="380,1200 919,912 919,1200" fill="var(--red)"/>
    <line x1="380" y1="1200" x2="919" y2="912" stroke="var(--white)" stroke-width="9"/>
    <g role="img" aria-label="Cartoon green germ character">
      <ellipse cx="775" cy="1000" rx="92" ry="72" fill="var(--white)"/>
      <ellipse cx="775" cy="1000" rx="84" ry="64" fill="var(--germ-green)"/>
    </g>
    <g role="img" aria-label="Cartoon spiky orange germ character">
      <circle cx="410" cy="1138" r="72" fill="var(--white)"/>
      <circle cx="410" cy="1138" r="63" fill="var(--germ-orange)"/>
    </g>
  </svg>

  <p class="intro display">We<br>want<br>to provide<br>a service<br>power washing<br>wheelie bins for the<br>hotel and catering trade<br>and domestic<br>wheelie bins.</p>

  <div class="brand-badge">Snapwell</div>

  <h1 class="headline display">Snapwell<br>Mite<br>Solution</h1>

  <p class="text-line display">Texting information to <span class="phone">07912448731</span>.eg KT37QB the pub black dumpster tuesday.</p>

  <p class="hazard">Salmonella ecoli influenza potentially contaminate anything else thatmay touch including other people or risk cross contamination by spreading the germs to door handles etc.</p>

  <h2 class="form-title">Registration Form</h2>
  <p class="field" style="top:835px">Postcode</p>
  <p class="field" style="top:905px">House number</p>
  <p class="field" style="top:977px">What day their bins<br>are emptied</p>
  <p class="form-note">We will follow the waste disposal vehicle and clean the bin when empty.</p>

  <p class="prices">
    <span class="line" style="left:395px;top:722px">4 wheele bin (dumpster) costs <span class="price">£10</span>for</span>
    <span class="line" style="left:393px;top:757px">thefirst clean and <span class="price">£5</span> per subsequent</span>
    <span class="line" style="left:437px;top:792px">clean and a 2 wheele bin (wheelie) costs</span>
    <span class="line" style="left:437px;top:820px">£6 for the first clean and <span class="price">£3</span> per</span>
    <span class="line" style="left:442px;top:858px">subsequent clean.</span>
  </p>

  <p class="filler">Lorem Ipsum is simply<br>dummy text of the printing<br>and typesetting industry.</p>

  <p class="web">
    <svg width="22" height="22" viewBox="0 0 22 22" aria-hidden="true">
      <g fill="none" stroke="var(--white)" stroke-width="1.6">
        <circle cx="11" cy="11" r="9"/>
        <ellipse cx="11" cy="11" rx="4" ry="9"/>
        <line x1="2" y1="11" x2="20" y2="11"/>
      </g>
    </svg>
    www.snapwell-bins.com
  </p>
</main>
</body>
</html>
```